Minimalist Sign Design (24” X 24”)

I am wanting to redesign our yard signs to be very clean, attractive, eye catching, and readable (imagine driving by a home with a sign In yard). We paint homes. I am hoping to have a design that incorporates our brand colors in a clean, professional way that represents our company. Clean, concise, easily read from a distance.

Target Market(s)

Homeowners

Industry/Entity Type

Painting And Decorating

Font styles to use
Sans Serif

Requirements
Must have
• Phone Number: (555) 014-7391
• Free Consultations
• Makeover in progress!
• Brand colors:
• Hunter Green: #355e3b
• Black
• White
Nice to have
• Would like the hunter green to he background color of sign. Can make logo white to stand out with the green.
Should not have
• Too busy or unable to read text

```html
<!DOCTYPE html>
<html lang="en">
<head>
<meta charset="utf-8">
<title>Makeover in Progress Yard Sign</title>
<link rel="stylesheet" href="https://fonts.googleapis.com/css2?family=Montserrat:wght@500;600;700;800&display=swap">
<style>
  :root {
    --hunter-green: #355e3b;
    --ink: #000000;
    --paper: #ffffff;
    --surround: #231f20;
  }
  html, body {
    margin: 0;
    padding: 0;
    width: 1200px;
    height: 1200px;
    overflow: hidden;
    background: var(--surround);
  }
  .canvas {
    position: relative;
    width: 1200px;
    height: 1200px;
    background: var(--surround);
    font-family: "Montserrat", Arial, sans-serif;
  }
  .sign {
    position: absolute;
    left: 137px;
    top: 137px;
    width: 926px;
    height: 926px;
    background: var(--paper);
  }
  .headline-band {
    position: absolute;
    left: 29px;
    top: 28px;
    width: 868px;
    height: 101px;
    background: var(--hunter-green);
    display: flex;
    align-items: center;
    justify-content: center;
  }
  .headline {
    margin: 0;
    color: var(--paper);
    font-weight: 700;
    font-size: 59px;
    letter-spacing: -0.5px;
    line-height: 1;
    white-space: nowrap;
  }
  .brand {
    position: absolute;
    left: 0;
    top: 192px;
    width: 926px;
    height: 440px;
    display: flex;
    align-items: center;
    justify-content: center;
    gap: 30px;
  }
  .brand-dot {
    width: 64px;
    height: 64px;
    border-radius: 50%;
    background: var(--ink);
    flex: none;
  }
  .brand-name {
    color: var(--ink);
    font-weight: 600;
    font-size: 92px;
    line-height: 1.08;
    letter-spacing: 8px;
    text-transform: uppercase;
    white-space: nowrap;
  }
  .brand-name span {
    display: block;
  }
  .offer {
    position: absolute;
    left: 33px;
    top: 683px;
    width: 860px;
    margin: 0;
    text-align: center;
    color: var(--hunter-green);
    font-weight: 800;
    font-size: 75px;
    line-height: 1;
    letter-spacing: -1px;
    white-space: nowrap;
  }
  .divider {
    position: absolute;
    left: 34px;
    top: 769px;
    width: 859px;
    height: 2px;
    background: var(--ink);
  }
  .contact {
    position: absolute;
    left: 38px;
    top: 780px;
    width: 855px;
    height: 96px;
    display: flex;
    align-items: center;
    justify-content: flex-start;
    gap: 14px;
  }
  .phone-icon {
    width: 73px;
    height: 73px;
    flex: none;
  }
  .phone-number {
    color: var(--ink);
    font-weight: 500;
    font-size: 108px;
    line-height: 1;
    letter-spacing: 0;
    white-space: nowrap;
  }
  .footer-band {
    position: absolute;
    left: 0;
    bottom: 0;
    width: 926px;
    height: 33px;
    background: var(--hunter-green);
  }
</style>
</head>
<body>
<div class="canvas">
  <div class="sign">
    <div class="headline-band">
      <h1 class="headline">MAKEOVER IN PROGRESS!</h1>
    </div>

    <div class="brand">
      <span class="brand-dot"></span>
      <div class="brand-name"><span>Keystone</span><span>Painting</span></div>
    </div>

    <p class="offer">FREE CONSULTATION</p>
    <div class="divider"></div>

    <div class="contact">
      <svg class="phone-icon" viewBox="0 0 100 100" aria-hidden="true">
        <circle cx="50" cy="50" r="50" fill="var(--ink)"/>
        <path d="M30 24c3-2 7-2 9 1l6 10c2 3 1 6-2 8l-4 3c3 8 9 14 17 18l3-4c2-3 5-4 8-2l10 6c3 2 3 6 1 9l-4 5c-3 3-8 4-13 2C44 74 28 58 22 40c-2-5-1-10 2-13z" fill="var(--paper)"/>
        <path d="M56 26a20 20 0 0 1 18 18" stroke="var(--paper)" stroke-width="4" fill="none" stroke-linecap="round"/>
        <path d="M56 35a11 11 0 0 1 9 9" stroke="var(--paper)" stroke-width="4" fill="none" stroke-linecap="round"/>
        <path d="M57 17a29 29 0 0 1 26 26" stroke="var(--paper)" stroke-width="4" fill="none" stroke-linecap="round"/>
      </svg>
      <span class="phone-number">(555) 014-7391</span>
    </div>

    <div class="footer-band"></div>
  </div>
</div>
</body>
</html>
```